Business Card Design

A card that's appealing to realtors and home buyers..
Something that's memorable,attractive, yet simple.

Home Inspection business.
Name of co. Birchwell Home Inspections
Serving Kern, Los Angeles, Santa Barbara & Ventura counties
NRQB Certified Inspectors (Use NRQB certified logo)
http://nrqb-example.com/logos/newlogos/NRQB_Logo008.gif
Mark Ollivane
555 314-2760
Gavin Ollivane
555 492-1835
Email :birchwellinspections@mailbox-example.com
Also use slogan: Providing peace of mind

```html
<!DOCTYPE html>
<html lang="en">
<head>
<meta charset="utf-8">
<title>Birchwell Home Inspections – Business Cards</title>
<link rel="stylesheet" href="https://fonts.googleapis.com/css2?family=Cinzel:wght@400&family=Michroma&display=swap">
<style>
  :root {
    --page: #e4e5e7;
    --card: #ffffff;
    --teal: #1d8fb3;
    --grey: #6f7073;
    --grey-light: #a9aaad;
    --ink: #4a4b4e;
  }
  * { box-sizing: border-box; margin: 0; padding: 0; }
  html, body { width: 1200px; height: 771px; overflow: hidden; }
  body {
    background: var(--page);
    position: relative;
    font-family: "Michroma", "Arial", sans-serif;
  }
  .card {
    position: absolute;
    top: 231px;
    width: 540px;
    height: 309px;
    background: var(--card);
    box-shadow: 0 2px 8px rgba(0,0,0,.12);
    overflow: hidden;
  }
  .card--front { left: 40px; }
  .card--back { left: 620px; }

  .wordmark {
    font-family: "Cinzel", "Times New Roman", serif;
    font-weight: 400;
    color: var(--teal);
    text-align: center;
    line-height: 1;
  }
  .wordmark__name { display: block; letter-spacing: .18em; }
  .wordmark__tag { display: block; letter-spacing: .04em; }

  .card--front .wordmark { position: absolute; left: 0; right: 0; top: 112px; }
  .card--front .wordmark__name { font-size: 40px; }
  .card--front .wordmark__tag { font-size: 19px; margin-top: 8px; }
  .slogan {
    position: absolute; left: 0; right: 0; top: 200px;
    text-align: center; color: var(--grey);
    font-size: 9px; letter-spacing: .12em;
  }

  .card--back .swoosh { position: absolute; inset: 0; }
  .card--back .wordmark { position: absolute; left: 250px; top: 26px; width: 230px; }
  .card--back .wordmark__name { font-size: 26px; }
  .card--back .wordmark__tag { font-size: 12px; margin-top: 5px; }

  .people {
    position: absolute; right: 290px; top: 96px;
    text-align: right; color: var(--ink);
    font-size: 9px; line-height: 1.6; letter-spacing: .06em;
    list-style: none;
  }
  .people li + li { margin-top: 8px; }
  .people__name { font-size: 11px; letter-spacing: .1em; }

  .divider {
    position: absolute; left: 262px; top: 94px;
    width: 1px; height: 94px; background: var(--grey-light);
  }

  .contacts {
    position: absolute; left: 274px; top: 96px;
    list-style: none; color: var(--ink);
    font-size: 8px; letter-spacing: .04em;
  }
  .contacts li { display: flex; align-items: center; min-height: 18px; }
  .contacts .email { font-size: 7px; letter-spacing: 0; }
  .contacts svg { width: 11px; height: 11px; margin-right: 7px; flex: none; }
  .badge { width: 11px; height: 11px; margin-right: 7px; border-radius: 50%; background: var(--teal); flex: none; }
  .area { display: block; line-height: 1.6; padding-left: 18px; font-size: 7.5px; }
</style>
</head>
<body>

<section class="card card--front" aria-label="Card front">
  <div class="wordmark">
    <span class="wordmark__name">BIRCHWELL</span>
    <span class="wordmark__tag">Home Inspections</span>
  </div>
  <p class="slogan">PROVIDING PEACE OF MIND</p>
</section>

<section class="card card--back" aria-label="Card back">
  <svg class="swoosh" viewBox="0 0 540 309" preserveAspectRatio="none" aria-hidden="true">
    <path d="M0,188 C130,245 300,275 540,266 L540,309 L0,309 Z" fill="var(--teal)"/>
    <path d="M0,222 C150,262 320,285 540,277 L540,309 L0,309 Z" fill="var(--card)"/>
    <path d="M170,309 C300,293 430,284 540,280 L540,309 Z" fill="var(--grey)"/>
    <path d="M0,232 C150,270 330,292 540,286" fill="none" stroke="var(--grey-light)" stroke-width="1.2"/>
  </svg>

  <div class="wordmark">
    <span class="wordmark__name">BIRCHWELL</span>
    <span class="wordmark__tag">Home Inspections</span>
  </div>

  <ul class="people">
    <li>
      <p class="people__name">MARK OLLIVANE</p>
      <p>555 314-2760</p>
    </li>
    <li>
      <p class="people__name">GAVIN OLLIVANE</p>
      <p>555 492-1835</p>
    </li>
  </ul>

  <div class="divider"></div>

  <ul class="contacts">
    <li class="email">
      <svg viewBox="0 0 12 12" aria-hidden="true"><circle cx="6" cy="6" r="6" fill="var(--grey)"/><rect x="3" y="4" width="6" height="4.2" fill="#fff"/><path d="M3,4 L6,6.4 L9,4" fill="none" stroke="var(--grey)" stroke-width=".8"/></svg>
      birchwellinspections@mailbox-example.com
    </li>
    <li>
      <span class="badge" role="img" aria-label="Certification badge"></span>
      NRQB CERTIFIED INSPECTORS
    </li>
    <li>
      <svg viewBox="0 0 12 12" aria-hidden="true"><circle cx="6" cy="6" r="6" fill="var(--grey)"/><path d="M6,2.6 C4.4,2.6 3.5,3.8 3.5,5 C3.5,6.6 6,9.4 6,9.4 C6,9.4 8.5,6.6 8.5,5 C8.5,3.8 7.6,2.6 6,2.6 Z" fill="#fff"/><circle cx="6" cy="5" r="1" fill="var(--grey)"/></svg>
      SERVING
    </li>
    <li style="display:block">
      <span class="area">KERN, LOS ANGELES,</span>
      <span class="area">SANTA BARBARA &amp; VENTURA COUNTIES</span>
    </li>
  </ul>
</section>

</body>
</html>
```